Business card for wedding & event planning company

I'm looking for a well designed double sided business card to represent my wedding and event planning company.

It should include the fact we manage the following events:
Weddings, birthdays, conferences, product launches, fashion shows & conventions
in the following areas:
Wiltshire, Oxfordshire, Berkshire & London

My contact details to be included are:

Moira Pennock
07715 482036
moira@amberlarkcelebrations.co.uk
www.amberlarkcelebrations.co.uk

My logo can be found at the following Filevaultex location:
AI file: https://www.filevaultex.com/s/k4mprt8wn31b7hz/brandlogo_sourcefile.ai?dl=0
PNG file:
https://www.filevaultex.com/s/h9qsle2vbx07mnd/brandlogo_image.png?dl=0

Target Market(s)

women aged 30-55

Industry/Entity Type

Wedding

Contact Information for Business Card

in the following areas:

Moira Pennock
Event Planner
07715 482036

Font styles to use
Serif
Sans Serif
Script

Requirements
Must have
• Purple and white colour scheme
Should not have
• Black background
• Please don't submit any of the see-through business card designs.

```html
<!DOCTYPE html>
<html lang="en">
<head>
<meta charset="utf-8">
<title>Amber Lark Celebrations – Business Card</title>
<link rel="stylesheet" href="https://fonts.googleapis.com/css2?family=Cormorant+Garamond:wght@500&family=Noto+Sans:wght@400&display=swap">
<style>
  :root {
    --page: #ffffff;
    --card: #dfc7e4;
    --card-edge: #111111;
    --plum: #8a3a9c;
    --plum-dark: #6e1f82;
    --plum-line: #9b4aae;
    --ink: #1a1a1a;
    --band-light: #e4cfe8;
    --band-deep: #b978c6;
    --ghost: #d6bcdc;
  }
  * { box-sizing: border-box; margin: 0; padding: 0; }
  html, body {
    width: 1200px; height: 353px; overflow: hidden;
    background: var(--page);
  }
  .sheet { position: relative; width: 1200px; height: 353px; }
  .card {
    position: absolute; top: 6px; height: 345px;
    background: var(--card);
    border: 3px solid var(--card-edge);
    overflow: hidden;
  }
  .card--front { left: 50px; width: 538px; }
  .card--back { left: 622px; width: 536px; }

  .ghost-motif {
    position: absolute; border-radius: 50%;
    background: radial-gradient(ellipse at center, var(--ghost) 0%, rgba(214,188,220,0) 70%);
  }

  .brand { position: absolute; text-align: center; font-family: "Cormorant Garamond", serif; font-weight: 500; color: var(--plum); }
  .brand__mark { display: block; margin: 0 auto; border: 2px solid var(--plum); border-radius: 50%; }
  .brand__name { display: block; text-transform: uppercase; line-height: 1; }
  .brand__sub { display: flex; align-items: center; gap: 8px; text-transform: uppercase; line-height: 1; }
  .brand__sub::before, .brand__sub::after { content: ""; flex: 1; height: 1px; background: var(--plum); }

  .front-brand { left: 150px; top: 36px; width: 300px; }
  .front-brand .brand__mark { width: 108px; height: 108px; }
  .front-brand .brand__name { font-size: 52px; margin-top: 22px; }
  .front-brand .brand__sub { font-size: 20px; letter-spacing: 2px; margin-top: 8px; }

  .pattern-band {
    position: absolute; left: 0; right: 0; bottom: 0; height: 73px;
    border-top: 4px solid var(--plum-dark);
    background: linear-gradient(180deg, var(--band-light), var(--band-deep) 55%, var(--band-light));
  }

  .back-brand { left: 12px; top: 8px; width: 204px; }
  .back-brand .brand__mark { width: 66px; height: 66px; }
  .back-brand .brand__name { font-size: 27px; margin-top: 14px; }
  .back-brand .brand__sub { font-size: 13px; letter-spacing: 1.5px; margin-top: 4px; }

  .services {
    position: absolute; left: 8px; top: 146px; width: 204px;
    list-style: none; font-family: "Noto Sans", sans-serif; font-size: 15px; color: var(--ink);
  }
  .services li { text-align: center; line-height: 18px; border-bottom: 2px solid var(--plum-line); }
  .services li:last-child { border-bottom: none; }

  .areas {
    position: absolute; left: 8px; right: 8px; top: 246px;
    border-top: 2px solid var(--plum-line);
    padding-top: 6px; text-align: right;
    font-family: "Noto Sans", sans-serif; font-size: 11px; color: var(--ink);
  }

  .contact-band {
    position: absolute; left: 0; right: 0; bottom: 0; height: 66px;
    border-top: 4px solid var(--plum-dark);
    background: var(--band-light);
    font-family: "Noto Sans", sans-serif; color: var(--ink);
  }
  .contact-band__person { position: absolute; left: 12px; top: 6px; font-size: 20px; line-height: 25px; }
  .contact-band__ring-motif {
    position: absolute; left: 170px; top: 6px; width: 76px; height: 50px; border-radius: 25px;
    background: linear-gradient(90deg, var(--band-light), var(--band-deep), var(--band-light));
  }
  .contact-band__online { position: absolute; right: 10px; top: 10px; text-align: right; font-size: 15px; line-height: 19px; }
</style>
</head>
<body>
<main class="sheet">
  <section class="card card--front" aria-label="Card front">
    <div class="ghost-motif" role="img" aria-label="Faint soft decorative motif" style="left:-20px; top:30px; width:260px; height:240px;"></div>
    <div class="brand front-brand">
      <span class="brand__mark"></span>
      <span class="brand__name">Amber Lark</span>
      <span class="brand__sub">Celebrations</span>
    </div>
    <div class="pattern-band" role="img" aria-label="Band of interlocking purple ring pattern"></div>
  </section>

  <section class="card card--back" aria-label="Card back">
    <div class="ghost-motif" role="img" aria-label="Faint soft decorative motif" style="left:270px; top:20px; width:260px; height:230px;"></div>
    <div class="brand back-brand">
      <span class="brand__mark"></span>
      <span class="brand__name">Amber Lark</span>
      <span class="brand__sub">Celebrations</span>
    </div>
    <ul class="services">
      <li>Weddings</li>
      <li>Birthdays</li>
      <li>Conferences</li>
      <li>Product Launches</li>
      <li>Fashion Shows &amp;</li>
      <li>Conventions</li>
    </ul>
    <p class="areas">Wiltshire, Oxfordshire, Berkshire &amp; London</p>
    <div class="contact-band">
      <p class="contact-band__person">Moira Pennock<br>07715 482036</p>
      <div class="contact-band__ring-motif" role="img" aria-label="Pair of interlocking purple rings"></div>
      <p class="contact-band__online">moira@amberlarkcelebrations.co.uk<br>www.amberlarkcelebrations.co.uk</p>
    </div>
  </section>
</main>
</body>
</html>
```